Medical Internet Marketing Company Needs a Site!

We need a new, fresh website for our search engine optimization and social media marketing company. We specialize in helping medical practices, doctors, physicians, and hospitals with their online presence and web ranking. The site should lean towards being suited for these audiences.

We have several examples of website that we like as well as things that we like about them.

Here are sites that we enjoy.

www.brightwavepromo.com

It's a good design for the site all around. The videos, buttons, and images are all excellent. They did a fine job.

- We really like their "contact us" side bar and want to include one like it on the secondary pages.

www.kestrelgrow.net

- We don't like the "thickness" of the top navigation bar.
- We like the page colors, easy navigation, and big call to action phone number in the top right corner.

http://www.tulavo.com/

Out of all the examples provided, Tulavo is our favorite and closest look and style to what we are looking for.

- We really like the openness of the design, such as space between the text and background.

- We want a price page in a style very similar to their pricing page with the services listed and check-marks, etc. although we intend to have multiple service package columns much like Kestrel's SEO pricing page.

- The way the video fits into the home page header is very organized, simple, and attention grabbing. We intend to place a slider with videos here.

- We need a page design that will allow for an image slider like Tulavo's Features page.

Here's a great example of a medical internet marketing website: http://www.dorvanta.com/

Target Market(s)

Our target market is doctors, typically male and typically 40-45 years old. I

Industry/Entity Type

Marketing

Requirements
Must have
• The homepage should have a slider in the video. Interior pages should have a video in the very top similar to how they do it on www.brightwavepromo.com

The top navigation tabs needed are:
- Home
- Solutions
- Resources
- About
- Why Zentrol
- Contact

The sidebar should have a GREAT call to action in it on interior pages.

There should be one interior page that is similar to this - http://www.tulavo.com/pricing/

There needs to be a page with multiple boxes that take up a row of the web page's body. This page will house all the case studies similar to brightwave promo's: http://www.brightwavepromo.com/success-stories/case-studies/ The one exception is we want the case studies to be inside of "boxes" instead of between horizontal lines like brightwave promo's.
Nice to have
• Color, professional, and clean. GREAT use of calls to actions.

```html
<!DOCTYPE html>
<html lang="fr">
<head>
<meta charset="utf-8">
<title>Zentrol — Medical Internet Marketing</title>
<link rel="stylesheet" href="https://fonts.googleapis.com/css2?family=Ubuntu:wght@300;400;500;700&display=swap">
<style>
:root{
  --sky-top:#bfe0f5;
  --sky-mid:#9fcdee;
  --hero-text:#1f5d92;
  --grey-logo:#8e969e;
  --teal:#2f9f88;
  --teal-dark:#258874;
  --gold:#d9a10f;
  --gold-light:#f0be2c;
  --maps:#d09b12;
  --doctor:#5cb6e0;
  --social:#8cbf26;
  --mobile:#3aa18a;
  --band:#ececec;
  --footer:#3b3b3b;
  --footer-line:#2c2c2c;
  --footer-text:#dcdcdc;
  --body-text:#333;
}
*{box-sizing:border-box;margin:0;padding:0}
html,body{width:1136px;height:1200px;overflow:hidden}
body{position:relative;font-family:"Ubuntu",sans-serif;color:var(--body-text);background:#fff}
a{color:inherit;text-decoration:none}
.abs{position:absolute}

.sky{position:absolute;left:0;top:0;width:1136px;height:429px;background:linear-gradient(180deg,var(--sky-top) 0%,#b3d9f3 50%,var(--sky-mid) 100%)}
.light-band{position:absolute;left:0;top:429px;width:1136px;height:234px;background:linear-gradient(180deg,#f1f1f1 0%,#fff 100%)}

.brand{left:170px;top:32px;display:flex;align-items:center;gap:10px}
.brand-mark{width:26px;height:26px;background:var(--grey-logo)}
.brand-name{font-size:32px;font-weight:500;letter-spacing:3px;color:var(--grey-logo)}

.nav{left:477px;top:36px;display:flex;align-items:center;font-size:10.5px;color:#111}
.nav a{padding:5px 0;margin-right:35px}
.nav a.active{background:linear-gradient(#3a3a3a,#111);color:#fff;padding:5px 15px;border-radius:6px;margin-right:18px}

.hero{left:170px;top:96px;width:795px;height:333px;background:linear-gradient(180deg,#8ec3ea 0%,#a8d2f1 60%,#b9dbf4 100%);box-shadow:0 0 8px rgba(70,130,180,.25)}
.hero-title{left:190px;top:120px;color:var(--hero-text);font-size:21px;line-height:30px;font-weight:400}
.hero-title b{font-weight:700;font-size:25px}
.hero-copy{left:190px;top:222px;width:260px;font-size:12px;line-height:22px;color:var(--hero-text);font-weight:300}
.signup{left:190px;top:306px;width:196px;height:46px;background:linear-gradient(#fff,#ececec);border-radius:3px;box-shadow:0 1px 3px rgba(0,0,0,.25);font-size:19px;font-weight:300;color:#111;display:flex;align-items:center;justify-content:center}

.video{left:474px;top:118px;width:471px;height:235px;background:linear-gradient(120deg,#f4efe9 0%,#e9eef3 55%,#cfe3f1 100%);border:1px solid #fff;box-shadow:0 0 6px rgba(0,0,0,.2)}
.player{left:489px;top:303px;width:441px;height:38px}
.dots{left:706px;top:365px;display:flex;gap:5px}
.dots span{width:8px;height:8px;border-radius:50%;background:#8fbbe0}
.dots span:first-child{background:#333}

.feature{top:396px;width:180px}
.feature .badge{width:64px;height:64px;border-radius:50%;border:4px solid #fff;box-shadow:0 1px 4px rgba(0,0,0,.25);margin-left:-6px;display:flex;align-items:center;justify-content:center}
.feature h3{margin-top:12px;font-size:16px;font-weight:400;line-height:20px}
.feature p{margin-top:16px;font-size:10px;line-height:12.7px;color:#222;width:140px}
.feature .more{display:block;margin-top:19px;font-size:12px;color:#111}
.arrow{top:514px}

.band{left:0;top:663px;width:1136px;height:98px;background:var(--band);border-top:1px solid #ddd;border-bottom:1px solid #ddd}
.seal{left:176px;top:643px;width:134px;height:134px;border-radius:50%;background:#6b5446}
.seal-inner{left:188px;top:655px;width:110px;height:110px;border-radius:50%;background:#f3ede5;border:3px solid #a89484}
.guarantee{left:325px;top:684px;font-size:24px;line-height:29px;color:#4a4a4a;font-weight:300}
.guarantee b{font-weight:700}
.cta{top:686px;height:53px;border-radius:3px;color:#fff;font-weight:300;display:flex;align-items:center;justify-content:center;text-align:center;box-shadow:0 2px 3px rgba(0,0,0,.25)}
.cta-contact{left:676px;width:139px;background:linear-gradient(var(--teal),var(--teal-dark));font-size:21px}
.cta-plans{left:825px;width:138px;background:linear-gradient(var(--gold-light),var(--gold));font-size:19px;line-height:19px}

.welcome{left:173px;top:803px;width:495px}
.welcome h2,.testimonials h2{font-size:15.5px;font-weight:400;color:#333}
.welcome p{margin-top:13px;font-size:10px;line-height:12.8px;color:#333}
.welcome h2+p{margin-top:14px}
.divider{left:698px;top:800px;width:1px;height:202px;background:#e2e2e2}
.testimonials{left:728px;top:803px;width:222px}
.testimonials .date{margin-top:14px;font-size:11px}
.testimonials p{font-size:10px;line-height:12.6px;margin-top:3px}
.testimonials .who{font-style:italic;font-size:10.5px;margin-top:1px}
.testimonials .more{display:block;margin-top:15px;font-size:12px;color:#111}

.footer{left:0;top:1030px;width:1136px;height:170px;background:var(--footer)}
.fcol-line{top:1030px;width:2px;height:170px;background:var(--footer-line)}
.flinks{left:183px;top:1071px;font-size:9.5px;line-height:18.5px;color:var(--footer-text)}
.social{left:183px;top:1137px;display:flex;gap:7px}
.social span{width:26px;height:26px;border-radius:3px}
.contact-info{left:546px;top:1053px;font-size:11px;line-height:24.7px;color:var(--footer-text);font-style:normal}
.foot-brand{left:782px;top:1097px;display:flex;align-items:center;gap:8px}
.foot-brand .brand-mark{width:22px;height:22px;background:#8a8a8a}
.foot-brand .brand-name{font-size:27px;color:#8a8a8a}
</style>
</head>
<body>
<div class="sky"></div>
<div class="light-band"></div>

<header>
  <a class="abs brand" href="#"><span class="brand-mark"></span><span class="brand-name">ZENTROL</span></a>
  <nav class="abs nav">
    <a class="active" href="#">HOME</a>
    <a href="#">SOLUTIONS</a>
    <a href="#">RESOURCES</a>
    <a href="#">ABOUT</a>
    <a href="#">WHY ZENTROL</a>
    <a href="#" style="margin-right:0">CONTACT</a>
  </nav>
</header>

<section>
  <div class="abs hero"></div>
  <h1 class="abs hero-title">Put Your<br><b>Website</b> on Top<br>of <b>Findora</b> Seach Engine</h1>
  <p class="abs hero-copy">Le Lorem Ipsum est simplement du faux texte employé dans la composition et la mise en page avant impression.</p>
  <a class="abs signup" href="#">Sign Up for FREE !</a>

  <div class="abs video" role="img" aria-label="Video still of a smiling doctor with a stethoscope and medical staff caring for a patient in a bright clinic"></div>
  <svg class="abs player" viewBox="0 0 441 38" aria-label="Video controls">
    <defs>
      <linearGradient id="barFill" x1="0" y1="0" x2="0" y2="1"><stop offset="0" stop-color="#50555c"/><stop offset="1" stop-color="#272a2f"/></linearGradient>
    </defs>
    <rect x="0" y="0" width="441" height="38" rx="4" fill="url(#barFill)"/>
    <g fill="#e8e8e8">
      <rect x="16" y="13" width="2" height="12"/><path d="M28 13v12l-9-6z"/>
      <path d="M60 13v12l-9-6z" transform="translate(0 0)" opacity="0"/>
      <path d="M66 13v12l9-6z" opacity="0"/>
      <path d="M70 13v12l7-6z"/><rect x="77" y="13" width="2" height="12"/>
      <path d="M104 13v12l-7-6zM111 13v12l-7-6z"/>
      <path d="M120 13v12l7-6zM127 13v12l7-6z"/>
    </g>
    <circle cx="46" cy="19" r="12" fill="#1c1d20" stroke="#111" stroke-width="2"/>
    <path d="M42 12l10 7-10 7z" fill="#fff"/>
    <line x1="88" y1="9" x2="88" y2="29" stroke="#22252a"/>
    <line x1="143" y1="9" x2="143" y2="29" stroke="#22252a"/>
    <rect x="146" y="15" width="116" height="9" rx="1" fill="#5c6268"/>
    <rect x="146" y="15" width="25" height="9" rx="1" fill="#5db02e"/>
    <rect x="169" y="12" width="5" height="15" rx="1" fill="#d8d8d8"/>
    <text x="275" y="23" font-size="9.5" fill="#f0f0f0" font-family="Ubuntu, sans-serif">1:38 / 4:43</text>
    <line x1="340" y1="9" x2="340" y2="29" stroke="#22252a"/>
    <path d="M355 16h3l5-4v14l-5-4h-3z" fill="#e8e8e8"/>
    <path d="M366 15q3 4 0 8" stroke="#e8e8e8" fill="none" stroke-width="1.3"/>
    <rect x="377" y="14" width="45" height="10" rx="1" fill="#5c6268"/>
    <rect x="378" y="15" width="35" height="8" fill="#d5111e"/>
  </svg>
  <div class="abs dots"><span></span><span></span><span></span></div>
</section>

<section>
  <svg class="abs arrow" style="left:172px" width="14" height="16" aria-hidden="true"><path d="M13 0v16L0 8z" fill="#333"/></svg>
  <svg class="abs arrow" style="left:951px" width="14" height="16" aria-hidden="true"><path d="M0 0v16L13 8z" fill="#333"/></svg>

  <article class="abs feature" style="left:221px">
    <div class="badge" style="background:var(--mobile)">
      <svg width="20" height="26" viewBox="0 0 20 26"><rect x="2" y="1" width="16" height="24" rx="2" fill="#fff"/><rect x="5" y="4" width="10" height="7" fill="var(--mobile)"/><g fill="var(--mobile)"><circle cx="6" cy="15" r="1.3"/><circle cx="10" cy="15" r="1.3"/><circle cx="14" cy="15" r="1.3"/><circle cx="6" cy="19" r="1.3"/><circle cx="10" cy="19" r="1.3"/><circle cx="14" cy="19" r="1.3"/></g></svg>
    </div>
    <h3 style="color:var(--mobile)">Mobile<br>Website</h3>
    <p>Le Lorem Ipsum est simple-ment du faux texte employé dans la composition et la mise en page avant impres-sion.</p>
    <a class="more" href="#">read more ▸</a>
  </article>

  <article class="abs feature" style="left:409px">
    <div class="badge" style="background:var(--maps)">
      <svg width="24" height="30" viewBox="0 0 24 30"><path d="M12 1C6 1 2 5.5 2 11c0 7 10 18 10 18s10-11 10-18C22 5.5 18 1 12 1z" fill="#fff"/><circle cx="12" cy="11" r="4" fill="var(--maps)"/></svg>
    </div>
    <h3 style="color:var(--maps)">Maps &amp;<br>Reviews</h3>
    <p>Le Lorem Ipsum est simple-ment du faux texte employé dans la composition et la mise en page avant impres-sion.</p>
    <a class="more" href="#">read more ▸</a>
  </article>

  <article class="abs feature" style="left:597px">
    <div class="badge" style="background:var(--doctor)">
      <svg width="30" height="32" viewBox="0 0 30 32" fill="none" stroke="#fff" stroke-width="2"><path d="M8 3v8a6 6 0 0 0 12 0V3"/><path d="M14 17v6a5 5 0 0 0 10 0v-4"/><circle cx="24" cy="16" r="3"/><circle cx="8" cy="25" r="4"/></svg>
    </div>
    <h3 style="color:var(--doctor)">Doctor<br>Portal</h3>
    <p>Le Lorem Ipsum est simple-ment du faux texte employé dans la composition et la mise en page avant impres-sion.</p>
    <a class="more" href="#">read more ▸</a>
  </article>

  <article class="abs feature" style="left:785px">
    <div class="badge" style="background:var(--social)">
      <svg width="26" height="26" viewBox="0 0 26 26"><rect x="3" y="3" width="20" height="20" rx="4" fill="#fff"/></svg>
    </div>
    <h3 style="color:var(--social)">Socail Media<br>&amp; Blogs</h3>
    <p>Le Lorem Ipsum est simple-ment du faux texte employé dans la composition et la mise en page avant impres-sion.</p>
    <a class="more" href="#">read more ▸</a>
  </article>
</section>

<section>
  <div class="abs band"></div>
  <div class="abs seal" aria-hidden="true"></div>
  <div class="abs seal-inner" aria-hidden="true"></div>
  <h2 class="abs guarantee">OUR <b>100%</b><br><b>SATISFACTION</b> GURANTEE</h2>
  <a class="abs cta cta-contact" href="#">Contact Us</a>
  <a class="abs cta cta-plans" href="#">See plans<br>&amp; prices</a>
</section>

<section>
  <div class="abs welcome">
    <h2>Welcome to ZENTROL</h2>
    <p>Contrairement à une opinion répandue, le Lorem Ipsum n'est pas simplement du texte aléatoire. Il trouve ses racines dans une oeuvre de la littérature latine classique datant de 45 av. J.-C., le rendant vieux de 2000 ans.</p>
    <p>Un professeur du Westbrook College, en Ardenne, s'est intéressé à un des mots latins les plus obscurs, consectetur, extrait d'un passage du Lorem Ipsum, et en étudiant tous les usages de ce mot dans la littérature classique, découvrit la source incontestable du Lorem Ipsum.</p>
    <p>Contrairement à une opinion répandue, le Lorem Ipsum n'est pas simplement du texte aléatoire. Il trouve ses racines dans une oeuvre de la littérature latine classique datant de 45 av. J.-C., le rendant vieux de 2000 ans. Un professeur du Westbrook College, en Ardenne, s'est intéressé à un des mots latins les plus obscurs, consectetur, extrait d'un passage du Lorem Ipsum, et en étudiant tous les usages de ce mot dans la littérature classique, découvrit la source incontestable du Lorem Ipsum.</p>
  </div>
  <div class="abs divider"></div>
  <div class="abs testimonials">
    <h2>Testimonials</h2>
    <div class="date">21st Nov 2013</div>
    <p>Le Lorem Ipsum est simplement du faux texte employé dans la composition et la mise en page avant impression.</p>
    <div class="who">Martin Hale</div>
    <div class="date" style="margin-top:10px">21st Nov 2013</div>
    <p>Le Lorem Ipsum est simplement du faux texte employé dans.</p>
    <div class="who">Paul Denton</div>
    <a class="more" href="#">read more ▸</a>
  </div>
</section>

<footer>
  <div class="abs footer"></div>
  <div class="abs fcol-line" style="left:523px"></div>
  <div class="abs fcol-line" style="left:753px"></div>
  <div class="abs flinks">
    <div>Home &nbsp;|&nbsp; Solutions &nbsp;|&nbsp; Resources &nbsp;|&nbsp; About &nbsp;|&nbsp; Why Zentrol &nbsp;|&nbsp; Contact</div>
    <div>All content Copyright ©2012 ZENTROL</div>
    <div>Terms of Use | Privacy Policy</div>
  </div>
  <div class="abs social" aria-label="Social links">
    <span style="background:#3b6fb6"></span>
    <span style="background:#1f7fb5"></span>
    <span style="background:#d8372c"></span>
  </div>
  <address class="abs contact-info">
    ZENTROL, LLC<br>
    Direct - (555) 214 - 7305<br>
    Call - (555) 386 - 1942<br>
    https://www.zentrol.com<br>
    https://www.harlowcreek.com
  </address>
  <div class="abs foot-brand"><span class="brand-mark"></span><span class="brand-name">ZENTROL</span></div>
</footer>
</body>
</html>
```